Zielgruppe
Strandhaus mit Restaurant (Beach feeling)
Zielgruppe: gehoben, edel, teuer
Aufgabenstellung
Auf stilsicherheit und das es stylisch und gleichzeitig edel aussieht.
Format:
Breite 44,5
Höher 71
Text:
Logo oben gut sichtbar
Herzlich Willkommen! (andere Schriftart)
MONTAG - FREITAG
SAMSTAG - SONNTAG
Unsere Küche verwöhnt dich bis 21:00 Uhr - täglich frisch & mit Liebe gekocht.
Wolkenhain ist mehr als ein Ort - es ist ein Gefühl. (andere Schriftart)
Lindenmoor, Kastner Weg 58-60, 2700 Wiener Neustadt
www.wolkenhain-beispiel.at/reservieren

```html
<!DOCTYPE html>
<html lang="de">
<head>
<meta charset="utf-8">
<title>Wolkenhain – Öffnungszeiten</title>
<link rel="stylesheet" href="https://fonts.googleapis.com/css2?family=Kaushan+Script&family=Mr+Dafoe&family=Oswald:wght@500;600&display=swap">
<style>
  :root {
    --page: #ffffff;
    --sky-top: #5b3d70;
    --sky-rose: #d9727a;
    --sky-mist: #b3c7c2;
    --sky-gold: #f3c77c;
    --sky-coral: #e48a6c;
    --night: #2f2a5c;
    --deep: #3b2f63;
    --ink-light: #ffffff;
    --ink-dark: #2d2a5a;
    --shadow: rgba(30, 20, 50, 0.75);
  }
  * { margin: 0; padding: 0; box-sizing: border-box; }
  html, body {
    width: 1200px; height: 1200px; overflow: hidden;
    background: var(--page);
  }
  .poster {
    position: absolute;
    left: 279px; top: 87px;
    width: 648px; height: 1033px;
    overflow: hidden;
    color: var(--ink-light);
  }
  .poster__scene {
    position: absolute; inset: 0;
    background: linear-gradient(180deg,
        var(--sky-top) 0%,
        #8a5478 15%,
        var(--sky-rose) 30%,
        #c99a92 40%,
        var(--sky-mist) 47%,
        #c9c8a8 58%,
        var(--sky-gold) 68%,
        var(--sky-coral) 80%,
        var(--deep) 88%,
        var(--night) 100%);
  }
  .poster__scene::after {
    content: ""; position: absolute; inset: 0;
    background: linear-gradient(90deg, rgba(47,42,92,0.55) 0%, rgba(47,42,92,0) 22%, rgba(47,42,92,0) 78%, rgba(47,42,92,0.55) 100%);
  }
  .brand {
    position: absolute; left: 0; right: 0; top: 125px;
    text-align: center;
    font-family: "Kaushan Script", cursive;
    font-weight: 400;
    font-size: 64px; line-height: 1;
    color: var(--ink-light);
  }
  .welcome {
    position: absolute; left: 30px; right: 30px; top: 240px;
    text-align: center;
    font-family: "Mr Dafoe", cursive;
    font-weight: 400;
    font-size: 100px; line-height: 0.76;
    text-shadow: 0 4px 10px var(--shadow);
    transform: rotate(-3deg);
  }
  .hours__day {
    position: absolute; left: 0; right: 0;
    text-align: center;
    font-family: "Kaushan Script", cursive;
    font-size: 40px; line-height: 1;
    text-shadow: 0 3px 8px var(--shadow);
    z-index: 2;
  }
  .hours__time {
    position: absolute; left: 0; right: 0;
    text-align: center;
    font-family: "Oswald", sans-serif;
    font-weight: 600;
    font-size: 52px; line-height: 1;
    letter-spacing: 0.02em;
    text-shadow: 0 3px 10px var(--shadow);
    z-index: 2;
  }
  .hours__day--week { top: 432px; }
  .hours__time--week { top: 484px; }
  .hours__day--weekend { top: 552px; }
  .hours__time--weekend { top: 602px; }
  .kitchen-note {
    position: absolute;
    left: 392px; top: 676px;
    width: 194px; height: 194px;
    border-radius: 50%;
    background: var(--ink-light);
    color: var(--ink-dark);
    display: flex; align-items: center; justify-content: center;
    text-align: center;
    font-family: "Kaushan Script", cursive;
    font-size: 14px; line-height: 1.38;
    padding: 18px 14px;
    z-index: 1;
  }
  .address {
    position: absolute; left: 0; right: 0; top: 895px;
    text-align: center;
    font-family: "Oswald", sans-serif;
    font-style: normal;
    font-weight: 500;
    font-size: 21px; line-height: 30px;
    text-transform: uppercase;
    letter-spacing: 0.42em;
  }
  .address__line { display: block; }
  .address__line--web { letter-spacing: 0.26em; font-size: 19px; }
</style>
</head>
<body>
  <main class="poster">
    <div class="poster__scene" role="img" aria-label="Illustrierter Sonnenuntergang am Strand mit Palmensilhouetten, fliegenden Möwen und Meer"></div>

    <h1 class="brand">Wolkenhain</h1>

    <h2 class="welcome">Herzlich<br>Willkommen!</h2>

    <section class="hours">
      <p class="hours__day hours__day--week">Montag - Freitag</p>
      <p class="hours__time hours__time--week">11:00 - 00:00</p>
      <p class="hours__day hours__day--weekend">Samstag - Sonntag</p>
      <p class="hours__time hours__time--weekend">09:00 - 00:00</p>
    </section>

    <p class="kitchen-note">Unsere<br>Küche verwöhnt dich<br>bis 21:00 Uhr - täglich<br>frisch &amp; mit Liebe gekocht.<br>Wolkenhain ist mehr<br>als ein Ort - es ist<br>ein Gefühl.</p>

    <address class="address">
      <span class="address__line">Lindenmoor, Kastner Weg 58-60</span>
      <span class="address__line">2700 Wiener Neustadt</span>
      <span class="address__line address__line--web">www.wolkenhain-beispiel.at/reservieren</span>
    </address>
  </main>
</body>
</html>
```